Real Estate investment company needs billboard designs

This is our website: https://velmarkpropertygroup.com/
We are looking for some billboard concepts that uses our CEO in the design. I have attached some images and 1 billboard design that someone in our industry uses, but we don't want it exactly like his.

Industry/Entity Type

real estate

Colors

Designer to choose colors to be used in the design.

Requirements
Must have
• Company colors from websiute

```html
<!DOCTYPE html>
<html lang="en">
<head>
<meta charset="UTF-8">
<title>Velmark Property Group – Billboard</title>
<link rel="stylesheet" href="https://fonts.googleapis.com/css2?family=Barlow+Semi+Condensed:wght@600;700&display=swap">
<style>
  :root {
    --page-bg: #e6e6e6;
    --brand-red: #ec1c24;
    --brand-navy: #0e1d43;
    --white: #ffffff;
    --photo-light: #c9d3e0;
    --photo-dark: #7f93ad;
  }
  * { margin: 0; padding: 0; box-sizing: border-box; }
  html, body {
    width: 1200px;
    height: 1200px;
    overflow: hidden;
    background: var(--page-bg);
    font-family: "Barlow Semi Condensed", Arial, sans-serif;
  }
  .billboard {
    position: absolute;
    left: 72px;
    top: 418px;
    width: 1056px;
    height: 332px;
    background: var(--white);
  }
  .headline-band {
    position: absolute;
    left: 0; top: 0;
    width: 100%;
    height: 90px;
    background: var(--brand-red);
  }
  .offer-panel {
    position: absolute;
    left: 0; top: 96px;
    width: 100%;
    height: 236px;
    background: var(--brand-navy);
  }
  .ceo-photo {
    position: absolute;
    left: 108px;
    top: 4px;
    width: 264px;
    height: 328px;
    background: linear-gradient(180deg, var(--photo-light) 0%, var(--photo-dark) 100%);
    clip-path: polygon(84px 0, 166px 0, 172px 92px, 226px 112px, 248px 150px, 264px 190px, 264px 328px, 0 328px, 0 200px, 22px 170px, 42px 120px, 90px 92px, 84px 50px);
  }
  .headline {
    position: absolute;
    left: 294px;
    top: 6px;
    font-weight: 700;
    font-size: 72px;
    line-height: 76px;
    color: var(--white);
    letter-spacing: 1px;
    white-space: nowrap;
  }
  .headline .accent { color: var(--brand-navy); }
  .headline .mark { color: var(--brand-navy); margin-left: 8px; }
  .brand-name {
    position: absolute;
    left: 22px;
    top: 122px;
    color: var(--white);
    font-weight: 700;
    text-transform: uppercase;
    line-height: 1;
  }
  .brand-name .word-main { display: block; font-size: 24px; letter-spacing: 0.5px; }
  .brand-name .word-sub { display: block; font-size: 9px; letter-spacing: 1px; margin-top: 3px; }
  .offer-text {
    position: absolute;
    left: 403px;
    top: 105px;
    font-weight: 700;
    font-size: 62px;
    line-height: 72px;
    color: var(--white);
    text-transform: uppercase;
    white-space: nowrap;
  }
  .phone-pill {
    position: absolute;
    left: 404px;
    top: 268px;
    width: 358px;
    height: 40px;
    background: var(--white);
    border-radius: 6px;
    display: flex;
    align-items: center;
  }
  .phone-number {
    padding-left: 20px;
    font-weight: 700;
    font-size: 28px;
    letter-spacing: 3px;
    color: var(--brand-navy);
    flex: 1;
  }
  .call-tag {
    margin-right: 4px;
    width: 96px;
    height: 32px;
    background: var(--brand-navy);
    border-radius: 5px;
    color: var(--white);
    font-weight: 700;
    font-size: 24px;
    letter-spacing: 1.5px;
    display: flex;
    align-items: center;
    justify-content: center;
  }
</style>
</head>
<body>
  <section class="billboard">
    <div class="headline-band"></div>
    <div class="offer-panel"></div>
    <div class="ceo-photo" role="img" aria-label="Company CEO standing with arms crossed, wearing a light blue denim shirt"></div>
    <h1 class="headline">SELLING YOUR <span class="accent">HOME</span><span class="mark">?</span></h1>
    <div class="brand-name">
      <span class="word-main">Velmark</span>
      <span class="word-sub">Property Group</span>
    </div>
    <p class="offer-text">Get a cash offer,<br>same day.</p>
    <div class="phone-pill">
      <span class="phone-number">555-014-2290</span>
      <span class="call-tag">CALL</span>
    </div>
  </section>
</body>
</html>
```